Alterations to existing business card

Here is my current logo and I want the "cafe and bar" taken off with just the words Lumo and our slogan "Savour every sip" on the card, Plus the logo.
Our Current Business Card is currently 5.5cm by 5.5cm and would like it to remain like this thanks.
The loyalty card can be 10 squares with the logo specifying the 10th coffee free. I would like the cheapest option please.
Also on our business card would like the Facebook logo and instagram Logo with TEAHOUSELUMO27 as link to our photos on instagram.

Keep Colour schemes the same please.

On the business cards

Dale Hartwig Director
0427913608
dale27lumo@examplemail.com

Rosa Delacourt Principal
0428150973
roslumo@examplemail.com

Thanks Dale

```html
<!DOCTYPE html>
<html lang="en">
<head>
<meta charset="utf-8">
<title>Lumo — Business &amp; Loyalty Cards</title>
<link href="https://fonts.googleapis.com/css2?family=Questrial&display=swap" rel="stylesheet">
<style>
  :root {
    --backdrop: #4a4a4a;
    --paper: #ffffff;
    --ink: #111111;
    --gold-deep: #eba63c;
    --gold-mid: #f3c556;
    --gold-light: #f9e27e;
    --gold-text: #e9a93f;
    --stamp-fill: #ef9f2e;
  }
  * { box-sizing: border-box; margin: 0; padding: 0; }
  html, body { width: 1105px; height: 1200px; overflow: hidden; }
  body {
    background: var(--backdrop);
    font-family: "Questrial", "Century Gothic", sans-serif;
    color: var(--ink);
    position: relative;
  }
  .card {
    position: absolute;
    width: 449px;
    height: 449px;
    overflow: hidden;
  }
  .business-card { left: 124px; top: 110px; background: var(--gold-deep); }
  .loyalty-card {
    left: 500px; top: 628px;
    background: linear-gradient(90deg, var(--gold-deep), var(--gold-mid) 55%, var(--gold-light));
  }
  .card-swoosh { position: absolute; inset: 0; }

  .brand-ring {
    position: absolute;
    border-radius: 50%;
    display: flex; align-items: center; justify-content: center;
  }
  .business-card .brand-ring {
    left: 62px; top: 36px; width: 132px; height: 132px;
    border: 4px solid var(--gold-mid);
  }
  .brand-name {
    position: absolute;
    left: 40px; top: 168px;
    font-size: 58px;
    letter-spacing: 2px;
    line-height: 1;
    color: var(--ink);
  }
  .slogan {
    position: absolute;
    left: 42px; top: 232px;
    font-size: 14px;
    font-style: italic;
    letter-spacing: 1.5px;
    color: var(--gold-text);
  }
  .person-name {
    position: absolute;
    left: 42px; top: 264px;
    font-size: 27px;
    letter-spacing: 1px;
    color: var(--gold-text);
  }
  .person-role {
    position: absolute;
    left: 42px; top: 300px;
    font-size: 19px;
    letter-spacing: .5px;
  }
  .contact-list {
    position: absolute;
    right: 24px; top: 370px;
    list-style: none;
    text-align: right;
    font-size: 20px;
  }
  .contact-list li {
    display: flex; justify-content: flex-end; align-items: center;
    gap: 14px; height: 30px;
  }
  .contact-list svg { width: 18px; height: 22px; }

  .loyalty-card .brand-ring {
    left: 135px; top: 27px; width: 166px; height: 166px;
    border: 4px solid var(--ink);
  }
  .loyalty-card .brand-ring span { font-size: 44px; letter-spacing: 2px; }

  .stamp-grid {
    position: absolute;
    left: 34px; top: 226px;
    display: grid;
    grid-template-columns: repeat(5, 64px);
    column-gap: 11px;
    row-gap: 16px;
  }
  .stamp {
    width: 64px; height: 64px;
    border-radius: 50%;
    border: 2px solid var(--ink);
    display: flex; align-items: center; justify-content: center;
  }
  .stamp-inner {
    width: 54px; height: 54px; border-radius: 50%;
    border: 1.5px solid var(--ink);
    display: flex; align-items: center; justify-content: center;
  }
  .stamp svg { width: 36px; height: 30px; }
  .stamp-free { background: var(--stamp-fill); }
  .stamp-free .stamp-inner { font-size: 18px; font-weight: 700; letter-spacing: .3px; }

  .social-handle {
    position: absolute;
    left: 44px; right: 44px; top: 398px;
    display: flex; align-items: center; gap: 10px;
    font-size: 19px; letter-spacing: 1px;
  }
  .social-handle .rule { flex: 1; height: 1px; background: var(--ink); opacity: .7; }
  .social-handle .dot { width: 20px; height: 20px; border-radius: 50%; background: var(--ink); }
</style>
</head>
<body>

<section class="card business-card" aria-label="Business card">
  <svg class="card-swoosh" viewBox="0 0 449 449" aria-hidden="true">
    <defs>
      <linearGradient id="goldBand" x1="0" x2="1" y1="0" y2="0">
        <stop offset="0" stop-color="#eba63c"/>
        <stop offset=".6" stop-color="#f3c556"/>
        <stop offset="1" stop-color="#f9e27e"/>
      </linearGradient>
    </defs>
    <rect width="449" height="449" fill="url(#goldBand)"/>
    <path d="M0,370 C170,370 380,352 449,150 L449,164 C390,372 170,384 0,378 Z" fill="#111"/>
    <path d="M0,0 H449 V150 C380,352 170,370 0,370 Z" fill="#fff"/>
  </svg>
  <div class="brand-ring" aria-hidden="true"></div>
  <div class="brand-name">LUMO</div>
  <div class="slogan">SAVOUR EVERY SIP</div>
  <div class="person-name">DALE HARTWIG</div>
  <div class="person-role">DIRECTOR</div>
  <ul class="contact-list">
    <li>0427913608
      <svg viewBox="0 0 14 22" aria-label="Phone"><rect x="1.5" y="1" width="11" height="20" rx="2" fill="none" stroke="#111" stroke-width="2"/><rect x="4" y="4" width="6" height="11" fill="#111"/></svg>
    </li>
    <li>dale27lumo@examplemail.com
      <svg viewBox="0 0 18 22" aria-label="Email"><rect x="1" y="6" width="16" height="11" fill="#111"/><path d="M1,6 L9,12 L17,6" fill="none" stroke="#fff" stroke-width="1.5"/></svg>
    </li>
  </ul>
</section>

<section class="card loyalty-card" aria-label="Loyalty card">
  <div class="brand-ring"><span>LUMO</span></div>
  <div class="stamp-grid">
    <div class="stamp"><div class="stamp-inner"><svg viewBox="0 0 36 30"><path d="M4,12 H26 V18 C26,24 21,27 15,27 C9,27 4,24 4,18 Z" fill="#111"/><path d="M26,14 C33,14 33,21 25,21" fill="none" stroke="#111" stroke-width="2"/><path d="M13,3 C11,6 16,7 14,10 M17,3 C15,6 20,7 18,10" fill="none" stroke="#111" stroke-width="1.2"/></svg></div></div>
    <div class="stamp"><div class="stamp-inner"><svg viewBox="0 0 36 30"><path d="M4,12 H26 V18 C26,24 21,27 15,27 C9,27 4,24 4,18 Z" fill="#111"/><path d="M26,14 C33,14 33,21 25,21" fill="none" stroke="#111" stroke-width="2"/><path d="M13,3 C11,6 16,7 14,10 M17,3 C15,6 20,7 18,10" fill="none" stroke="#111" stroke-width="1.2"/></svg></div></div>
    <div class="stamp"><div class="stamp-inner"><svg viewBox="0 0 36 30"><path d="M4,12 H26 V18 C26,24 21,27 15,27 C9,27 4,24 4,18 Z" fill="#111"/><path d="M26,14 C33,14 33,21 25,21" fill="none" stroke="#111" stroke-width="2"/><path d="M13,3 C11,6 16,7 14,10 M17,3 C15,6 20,7 18,10" fill="none" stroke="#111" stroke-width="1.2"/></svg></div></div>
    <div class="stamp"><div class="stamp-inner"><svg viewBox="0 0 36 30"><path d="M4,12 H26 V18 C26,24 21,27 15,27 C9,27 4,24 4,18 Z" fill="#111"/><path d="M26,14 C33,14 33,21 25,21" fill="none" stroke="#111" stroke-width="2"/><path d="M13,3 C11,6 16,7 14,10 M17,3 C15,6 20,7 18,10" fill="none" stroke="#111" stroke-width="1.2"/></svg></div></div>
    <div class="stamp"><div class="stamp-inner"><svg viewBox="0 0 36 30"><path d="M4,12 H26 V18 C26,24 21,27 15,27 C9,27 4,24 4,18 Z" fill="#111"/><path d="M26,14 C33,14 33,21 25,21" fill="none" stroke="#111" stroke-width="2"/><path d="M13,3 C11,6 16,7 14,10 M17,3 C15,6 20,7 18,10" fill="none" stroke="#111" stroke-width="1.2"/></svg></div></div>
    <div class="stamp"><div class="stamp-inner"><svg viewBox="0 0 36 30"><path d="M4,12 H26 V18 C26,24 21,27 15,27 C9,27 4,24 4,18 Z" fill="#111"/><path d="M26,14 C33,14 33,21 25,21" fill="none" stroke="#111" stroke-width="2"/><path d="M13,3 C11,6 16,7 14,10 M17,3 C15,6 20,7 18,10" fill="none" stroke="#111" stroke-width="1.2"/></svg></div></div>
    <div class="stamp"><div class="stamp-inner"><svg viewBox="0 0 36 30"><path d="M4,12 H26 V18 C26,24 21,27 15,27 C9,27 4,24 4,18 Z" fill="#111"/><path d="M26,14 C33,14 33,21 25,21" fill="none" stroke="#111" stroke-width="2"/><path d="M13,3 C11,6 16,7 14,10 M17,3 C15,6 20,7 18,10" fill="none" stroke="#111" stroke-width="1.2"/></svg></div></div>
    <div class="stamp"><div class="stamp-inner"><svg viewBox="0 0 36 30"><path d="M4,12 H26 V18 C26,24 21,27 15,27 C9,27 4,24 4,18 Z" fill="#111"/><path d="M26,14 C33,14 33,21 25,21" fill="none" stroke="#111" stroke-width="2"/><path d="M13,3 C11,6 16,7 14,10 M17,3 C15,6 20,7 18,10" fill="none" stroke="#111" stroke-width="1.2"/></svg></div></div>
    <div class="stamp"><div class="stamp-inner"><svg viewBox="0 0 36 30"><path d="M4,12 H26 V18 C26,24 21,27 15,27 C9,27 4,24 4,18 Z" fill="#111"/><path d="M26,14 C33,14 33,21 25,21" fill="none" stroke="#111" stroke-width="2"/><path d="M13,3 C11,6 16,7 14,10 M17,3 C15,6 20,7 18,10" fill="none" stroke="#111" stroke-width="1.2"/></svg></div></div>
    <div class="stamp stamp-free"><div class="stamp-inner">FREE</div></div>
  </div>
  <div class="social-handle">
    <span class="rule"></span>
    <span class="dot" aria-hidden="true"></span>
    <span>TEAHOUSELUMO27</span>
    <span class="rule"></span>
  </div>
</section>

</body>
</html>
```